BrookLark Wines - Label design for wine bottle

Logo and wine label design required for a wine label to be used on a bottle and merchandise
Name of company is BrookLark (one word). on the Label it is to have:
BrookLark
Waipara Pinot Noir
Label is named after a pit pony which was used in the mines to haul coal out from underground. They were known as the hardest working in the mines so the label is an ode to working hard and getting where you want to go. It also holds the connection to mining which is the profession in which we both work. We don’t want a picture of a horse in the label but happy for an abstract link to be there to a Pit Pony/Cart (wheel spoke) or Coal (eg pattern of the natural cleats of coal as the background). The logo should be somewhat of an abstract link to coal, not a direct image i.e coal wagon

Other font styles liked:
• FF Blur Light (open to others also)

Requirements
Must have
• Name of label BrookLark, abstract design as background with names on top
Nice to have
• Darker colours, greyscale, black and white
Should not have
• Picture of grapes of wine (eg glasses), Not overly busy or with alot of color

```html
<!DOCTYPE html>
<html lang="en">
<head>
<meta charset="utf-8">
<title>BrookLark Wines – Label</title>
<link rel="stylesheet" href="https://fonts.googleapis.com/css2?family=Jost:wght@300;400&display=swap">
<style>
  :root {
    --ink: #111111;
    --cream: #e6e2d6;
    --stone: #b9b5aa;
    --charcoal: #2a2a2a;
    --paper-top: #e9eaef;
    --paper-bottom: #ffffff;
  }
  * { margin: 0; padding: 0; box-sizing: border-box; }
  html, body { width: 1200px; height: 900px; overflow: hidden; }
  body {
    position: relative;
    background: linear-gradient(135deg, var(--paper-top) 0%, var(--paper-bottom) 70%);
    font-family: "Jost", sans-serif;
    color: var(--ink);
  }
  .brand-wordmark {
    position: absolute;
    left: 112px;
    top: 104px;
    font-family: "Jost", sans-serif;
    font-weight: 300;
    font-size: 46px;
    letter-spacing: 0.06em;
    color: var(--ink);
    line-height: 1;
  }
  .wine-label {
    position: absolute;
    left: 410px;
    top: 200px;
    width: 380px;
    height: 500px;
    background: var(--cream);
    overflow: hidden;
  }
  .label-pattern {
    position: absolute;
    inset: 0;
    background:
      linear-gradient(160deg, var(--stone) 0%, var(--charcoal) 45%, var(--stone) 70%, var(--charcoal) 100%);
  }
  .label-name-band {
    position: absolute;
    left: 0;
    top: 100px;
    width: 100%;
    height: 70px;
    background: var(--cream);
    display: flex;
    align-items: center;
    justify-content: center;
  }
  .label-name {
    font-family: "Jost", sans-serif;
    font-weight: 300;
    font-size: 44px;
    letter-spacing: 0.06em;
    color: var(--ink);
    line-height: 1;
  }
  .label-details {
    position: absolute;
    left: 24px;
    bottom: 26px;
    padding: 10px 14px;
    background: var(--cream);
    font-family: "Jost", sans-serif;
    font-weight: 400;
    font-size: 22px;
    line-height: 1.15;
    letter-spacing: 0.02em;
    text-transform: uppercase;
    color: var(--ink);
  }
  .label-details .variety { padding-left: 34px; }
</style>
</head>
<body>
  <div class="brand-wordmark">BrookLark</div>

  <section class="wine-label">
    <div class="label-pattern" role="img" aria-label="Abstract black and cream geometric pattern of blocks and stripes evoking coal cleats"></div>
    <div class="label-name-band">
      <span class="label-name">BrookLark</span>
    </div>
    <div class="label-details">
      <div class="variety">Syrah</div>
      <div class="region">Barossa 2019</div>
    </div>
  </section>
</body>
</html>
```